Stonefield Crew Brochure = SCB $$$

this brochure will be used for a canvassing campaign (door to door) appointment setting

the campaign will be for homeowners that would like to do any kind of improvement to their house - home improvement
from EXT paint or roof repair all the way to kitchen and bathroom remodeling

we want to catch the prospect eye with the brochure and to educate our prospect about the different ways they could improve their house step by step to their dream house

Target Market(s)

Homeowners
anyone who would like to improve or fix any part of their house

Industry/Entity Type

Home Improvement

Contact Information for Business Card

the green roof house blueprints on one side
the Stonefield Crew logo on the other side

Font styles to use
Serif
Decorative

Colors
ffffff
886aae
9bcb3b
e6e6e6

Requirements
Must have
• this is a TRI-FOLD brochure
• call for action -- schedule your free estimate
• or any idea that will lead to set up an appointment with our specialist
• LOOK AT MY WEBSITE TO UNDERSTAND MORE WHAT I LIKE
• WWW.THESTONEFIELDCREWS-EXAMPLE.COM
• services:
• Kitchen Renovations
• Bathroom Renovations
• Modern Landscaping
• Additions + in-law quarters
• Exterior paint +interior paint
• wood replacement + stucco repair
• roof repair
• railling and glass work
Nice to have
• the pictures I have uploaded can use as an example but im open to other ideas...
• THERE IS NO SUBSTITUTE FOR QUALITY.
• the picture of the women in the kitchen--
• i enjoy making food and spending time in my new kitchen, to see my whole family sitting down to eat dinner together in our perfect little kitchen make me so happy
Should not have
• the 2 brochures i have uploaded are for example only

```html
<!DOCTYPE html>
<html lang="en">
<head>
<meta charset="utf-8">
<title>Stonefield Crew Brochure</title>
<link href="https://fonts.googleapis.com/css2?family=Montserrat:wght@700;800&family=Raleway:wght@300;400;500;600;700&display=swap" rel="stylesheet">
<style>
  :root{
    --green:#8cc63f;
    --green-light:#a6d65a;
    --green-deep:#6fb32e;
    --ink:#1b1b1b;
    --grey-box:#d9d9d9;
    --text:#2e2e2e;
    --muted:#9a9a9a;
    --white:#ffffff;
    --globe:#2b8ccf;
    --stage:#e6e6e6;
  }
  *{box-sizing:border-box;margin:0;padding:0}
  html,body{width:1200px;height:980px;overflow:hidden;background:var(--stage)}
  body{font-family:"Raleway",sans-serif;color:var(--text)}
  .brochure{position:absolute;left:0;top:31px;width:1200px;height:917px;background:var(--white);overflow:hidden}
  .shapes{position:absolute;left:0;top:0;width:1200px;height:917px}
  .abs{position:absolute}

  /* left panel */
  .hero-line{font-family:"Montserrat",sans-serif;font-weight:800;color:var(--green);left:42px;width:303px;text-align:center;line-height:1}
  .hero-design{top:30px;font-size:49px;letter-spacing:-0.5px}
  .hero-build{top:77px;height:83px;background:var(--grey-box);color:var(--white);font-size:94px;line-height:86px;letter-spacing:-1px}
  .hero-inspire{top:164px;font-size:66px;letter-spacing:-1px}
  .passion{top:242px;left:0;width:391px;text-align:center;font-size:15.5px;line-height:21px;color:var(--text)}
  .section-title{font-family:"Montserrat",sans-serif;font-weight:700;color:var(--green)}
  .philosophy-title{top:316px;left:0;width:391px;text-align:center;font-size:21px}
  .philosophy-text{top:356px;left:25px;width:342px;font-size:13px;line-height:20.6px;text-align:justify;text-align-last:center}

  .services-card{top:790px;left:18px;width:300px;padding:9px 12px 10px;background:rgba(255,255,255,.93);border-left:4px solid var(--green)}
  .services-title{font-family:"Montserrat",sans-serif;font-weight:700;font-size:12.5px;color:var(--green);margin-bottom:5px;letter-spacing:.5px}
  .services-list{list-style:none;display:grid;grid-template-columns:1fr 1fr;column-gap:10px;row-gap:2px;font-size:10.5px;line-height:14px;color:var(--text)}
  .services-list li{display:flex;gap:5px;align-items:flex-start}
  .services-list li::before{content:"";flex:0 0 5px;height:5px;margin-top:5px;background:var(--green);border-radius:50%}

  /* middle panel */
  .dreams{top:40px;left:391px;width:396px;text-align:center;font-size:28px;font-weight:400;line-height:33px;color:var(--ink)}
  .dreams .accent{color:var(--green)}
  .testimonial-box{top:191px;left:416px;width:344px;height:245px;border:1.5px dashed #b5b5b5;border-radius:6px}
  .testimonial-title{top:163px;left:430px;width:316px;text-align:center;font-size:21px;line-height:24px;font-weight:800;background:var(--white)}
  .quote-open{top:208px;left:430px;font-family:"Montserrat",sans-serif;font-weight:800;font-size:64px;color:#c8c8c8;line-height:1}
  .testimonial-text{top:250px;left:433px;width:312px;font-size:12.8px;line-height:17.8px;text-align:justify;color:var(--text)}
  .quote-close{top:393px;left:558px;font-family:"Montserrat",sans-serif;font-weight:800;font-size:64px;color:#c8c8c8;line-height:1}
  .client-name{top:408px;left:650px;width:90px;text-align:right;font-family:"Montserrat",sans-serif;font-weight:700;font-size:13.5px;color:var(--green)}
  .stars{top:423px;left:430px;padding:0 4px;background:var(--white);color:var(--green);font-size:17px;letter-spacing:3px;line-height:22px}

  .brand-disc{top:606px;left:437px;width:104px;height:104px;border-radius:50%;background:var(--ink);border:4px solid var(--green)}
  .contact-name{top:636px;left:556px;font-family:"Montserrat",sans-serif;font-weight:700;font-size:16px;color:var(--green)}
  .contact-rule{top:660px;left:556px;width:30px;height:2px;background:var(--white)}
  .contact-list{top:670px;left:556px;width:226px;list-style:none;color:var(--white);font-size:11.5px;line-height:15px}
  .contact-list li{display:flex;align-items:flex-start;gap:7px;margin-bottom:7px;white-space:nowrap}
  .contact-list svg{flex:0 0 12px;margin-top:1px}
  .share-text{top:822px;left:408px;font-size:13.5px;line-height:18px;color:var(--text)}
  .social-row{top:880px;left:407px;display:flex;gap:6px}
  .social-row span{width:22px;height:22px;border-radius:50%;background:var(--green)}

  /* right panel */
  .logo-disc{top:21px;left:888px;width:68px;height:68px;border-radius:50%;background:var(--ink);border:3px solid var(--green)}
  .logo-name{top:30px;left:966px;color:var(--white);font-size:21px;font-weight:600;line-height:24px;letter-spacing:1px}
  .believe{top:541px;right:18px;text-align:right;font-size:21px;line-height:28px;color:var(--white);font-weight:400}
  .believe .accent{color:var(--green)}
  .tagline{left:814px;color:var(--white);line-height:1}
  .tag-light{font-family:"Raleway",sans-serif;font-weight:300}
  .tag-bold{font-family:"Montserrat",sans-serif;font-weight:800}
  .tag-1{top:643px;font-size:31px}
  .tag-2{top:671px;font-size:45px}
  .tag-3{top:713px;font-size:45px;display:flex;align-items:flex-end;gap:8px}
  .tag-3 .tag-light{font-size:32px;border-bottom:2px solid var(--white);padding-bottom:2px}
  .cta{top:776px;left:814px;padding:8px 16px;background:var(--ink);color:var(--white);font-family:"Montserrat",sans-serif;font-weight:700;font-size:13.5px;letter-spacing:.5px;border-radius:3px}
  .cta small{display:block;font-family:"Raleway",sans-serif;font-weight:500;font-size:11px;letter-spacing:0;color:var(--green-light);margin-top:2px}
  .web-footer{top:890px;left:889px;width:260px;display:flex;align-items:center;gap:8px;font-size:14.5px;color:var(--text);white-space:nowrap}
  .web-footer i{flex:1;height:1px;background:#bbb}
</style>
</head>
<body>
<main class="brochure">
  <svg class="shapes" viewBox="0 0 1337 1022" preserveAspectRatio="none">
    <defs>
      <linearGradient id="fadeLeft" x1="0" y1="0" x2="1" y2="1">
        <stop offset="0" stop-color="#ffffff"/><stop offset="1" stop-color="#eeeeee"/>
      </linearGradient>
      <linearGradient id="workersTone" x1="0" y1="0" x2="1" y2="1">
        <stop offset="0" stop-color="#eef1f3"/><stop offset=".55" stop-color="#d7dde3"/><stop offset="1" stop-color="#b9c4d2"/>
      </linearGradient>
      <linearGradient id="kitchenTone" x1="0" y1="0" x2="1" y2="1">
        <stop offset="0" stop-color="#f4f2ef"/><stop offset=".5" stop-color="#d9d4cf"/><stop offset="1" stop-color="#b9c2cf"/>
      </linearGradient>
      <linearGradient id="blackBand" x1="0" y1="0" x2="1" y2="1">
        <stop offset="0" stop-color="#2a2a2a"/><stop offset="1" stop-color="#111111"/>
      </linearGradient>
    </defs>
    <rect x="0" y="0" width="436" height="1022" fill="url(#fadeLeft)"/>
    <rect x="436" y="0" width="441" height="1022" fill="#fafafa"/>

    <g role="img" aria-label="Photo of two smiling painters in hard hats and blue overalls working in a bright room">
      <polygon points="0,560 210,662 436,552 436,1022 0,1022" fill="url(#workersTone)"/>
    </g>
    <polygon points="0,545 225,655 205,668 0,578" fill="var(--ink)"/>
    <polygon points="200,666 436,550 436,792" fill="var(--green)" opacity=".88"/>
    <polygon points="300,620 400,570 400,680" fill="var(--green-light)" opacity=".5"/>
    <line x1="290" y1="610" x2="436" y2="540" stroke="var(--green)" stroke-width="3"/>

    <polygon points="436,550 690,655 436,792" fill="var(--green-deep)"/>
    <polygon points="436,600 570,655 436,725" fill="var(--green-light)" opacity=".55"/>
    <polygon points="436,800 690,655 877,548 877,1022" fill="url(#blackBand)"/>
    <line x1="436" y1="540" x2="690" y2="648" stroke="var(--green)" stroke-width="2"/>
    <line x1="445" y1="812" x2="700" y2="940" stroke="var(--green)" stroke-width="4"/>
    <line x1="470" y1="800" x2="680" y2="905" stroke="var(--green)" stroke-width="2"/>

    <g role="img" aria-label="Photo of a smiling woman holding a mug in her bright white kitchen">
      <rect x="877" y="0" width="460" height="600" fill="url(#kitchenTone)"/>
    </g>
    <polygon points="877,0 992,0 877,121" fill="var(--green)"/>
    <polygon points="1222,0 1337,0 1337,121" fill="var(--green)"/>
    <polygon points="922,0 1287,0 1107,163" fill="var(--ink)"/>

    <polygon points="918,546 1337,500 1337,790 1160,665" fill="url(#blackBand)"/>
    <polygon points="877,546 1160,665 1337,790 1337,800 1000,1022 877,1022" fill="var(--green)"/>
    <polygon points="877,600 1040,680 877,800" fill="var(--green-light)" opacity=".45"/>
    <polygon points="900,900 1100,820 1000,1000" fill="var(--green-deep)" opacity=".4"/>
    <line x1="1020" y1="1022" x2="1337" y2="830" stroke="var(--green)" stroke-width="3"/>
    <line x1="1150" y1="990" x2="1337" y2="880" stroke="var(--green)" stroke-width="2"/>
  </svg>

  <!-- left panel -->
  <h1 class="abs hero-line hero-design">WE DESIGN</h1>
  <div class="abs hero-line hero-build">BUILD</div>
  <div class="abs hero-line hero-inspire">INSPIRE</div>
  <p class="abs passion">Building is our Passion.<br>Making Your Dreams into Reality is our Goal.</p>
  <h2 class="abs section-title philosophy-title">OUR PHILOSOPHY</h2>
  <p class="abs philosophy-text">We believe that every project deserves the same kind of attention, no matter if it’s a one room remodel or a new build of a multimillion dollar structure. To us, quality is achieving the best results, with the highest-grade material, at the lowest cost to you. That is how we define quality and that is what you’re getting with the Stonefield Crew.</p>

  <section class="abs services-card">
    <h3 class="services-title">OUR SERVICES</h3>
    <ul class="services-list">
      <li>Kitchen Renovations</li>
      <li>Bathroom Renovations</li>
      <li>Modern Landscaping</li>
      <li>Additions + In-Law Quarters</li>
      <li>Exterior + Interior Paint</li>
      <li>Wood Replacement + Stucco</li>
      <li>Roof Repair</li>
      <li>Railing + Glass Work</li>
    </ul>
  </section>

  <!-- middle panel -->
  <p class="abs dreams">Each day, more people<br><span class="accent">are living the life of<br>their dreams.</span></p>
  <div class="abs testimonial-box"></div>
  <h2 class="abs section-title testimonial-title">SEE WHAT OUR<br>CLIENTS ARE SAYING!</h2>
  <span class="abs quote-open">“</span>
  <p class="abs testimonial-text">They are excellent!!! They were on time everyday, professional, and by far the best priced bid. Owen initially met with us to give us a step by step process of our kitchen remodel and also incorporated some of his own ideas that made our kitchen look amazing. They worked with our budget which was the most important thing for us along with a nice kitchen. I would definitely recommend them.</p>
  <span class="abs quote-close">”</span>
  <span class="abs client-name">- MARCUS T.</span>
  <span class="abs stars">★★★★★</span>

  <div class="abs brand-disc"></div>
  <h3 class="abs contact-name">The Stonefield Crew</h3>
  <span class="abs contact-rule"></span>
  <ul class="abs contact-list">
    <li><svg width="12" height="12" viewBox="0 0 12 12"><path d="M6 0.5a4 4 0 0 1 4 4c0 3-4 7-4 7s-4-4-4-7a4 4 0 0 1 4-4z" fill="var(--green)"/><circle cx="6" cy="4.5" r="1.5" fill="var(--ink)"/></svg><span>418 Alder Creek Rd. Unit #3<br>Springvale, CA 90000</span></li>
    <li><svg width="12" height="12" viewBox="0 0 12 12"><circle cx="6" cy="6" r="6" fill="var(--green)"/><path d="M4 3l1.3 1.6-.8.9c.5 1 1.2 1.7 2.1 2.1l.9-.8L9 8l-.8 1C6 9 3 6 3 3.8z" fill="var(--ink)"/></svg><span>(555) 013-2840</span></li>
    <li><svg width="12" height="12" viewBox="0 0 12 12"><circle cx="6" cy="6" r="6" fill="var(--green)"/><rect x="3" y="4" width="6" height="4.5" fill="var(--ink)"/><path d="M3 4l3 2.4L9 4" stroke="var(--green)" stroke-width=".8" fill="none"/></svg><span>hi@stonefieldcrew-example.com</span></li>
    <li><svg width="12" height="12" viewBox="0 0 12 12"><circle cx="6" cy="6" r="6" fill="var(--globe)"/><circle cx="6" cy="6" r="3" stroke="var(--white)" stroke-width=".8" fill="none"/><line x1="3" y1="6" x2="9" y2="6" stroke="var(--white)" stroke-width=".8"/></svg><span>www.thestonefieldcrews-example.com</span></li>
  </ul>
  <p class="abs share-text">If you enjoyed the<br>experience, share with<br>your friends.</p>
  <div class="abs social-row"><span></span><span></span><span></span><span></span><span></span></div>

  <!-- right panel -->
  <div class="abs logo-disc"></div>
  <div class="abs logo-name">STONEFIELD<br>CREW</div>
  <p class="abs believe"><span class="accent">We believe</span><br>and live by our<br>words...</p>
  <div class="abs tagline tag-light tag-1">THERE IS NO</div>
  <div class="abs tagline tag-bold tag-2">SUBSTITUTE</div>
  <div class="abs tagline tag-3"><span class="tag-light">FOR</span><span class="tag-bold">QUALITY</span></div>
  <div class="abs cta">SCHEDULE YOUR FREE ESTIMATE<small>Call (555) 013-2840 to book a specialist</small></div>
  <div class="abs web-footer"><i></i><span>www.thestonefieldcrews-example.com</span><i></i></div>
</main>
</body>
</html>
```